Manufacturing Company WordPress Website Design

Looking for a modern WordPress design for a manufacturer of oil separation and coolant recycling products called BrightVane. This is a business-to-business marketer in the industrial manufacturing sector. BrightVane sells to CNC manufacturing companies and their products are known as some of the best tools in the world for skimming and separating floating oils, metallic fines, and other contaminants from industrial process fluids.

The winning design will be based on a responsive WP theme. Include the theme name if your design is selected by the client. Provide Home, Product and Case Study page views with your submission.

THE BRIGHTVANE BRAND
The BrightVane brand is all about connection and partnership. They are down-to-earth, relatable, helpful and fun to hang out with. The brand voice is humble, authentic and helpful and they are driven by connection, togetherness and inclusion.

The BrightVane target audience is plant managers, enterprise engineers and business owners in CNC machining manufacturing companies across a variety of industries (automotive, aerospace, energy, medical and transportation).

BrightVane is looking for a clean, modern website that better represents their brand with a more polished and professional design. It should be:
- responsive and mobile-friendly
- easily findable for key search criteria
- a source for improved lead generation for prospective sales
- more easily editable

A design that is oriented toward these goals will be selected as the winner.

The winning designer may be chosen to code the website, or to code the initial pages in the concept design.

Current Website:
https://brightvane-example.com/index.html

Competitors:
https://www.tovlex-example.com/
https://www.mundrel-example.com/
https://www.kelvaro-example.com/

Sites We Like:
https://northgatesteelworks-example.com/
- we like the clean layout of the home page in a grid-like design, simple header and footer, the parallax scrolling, and the mobile responsiveness.

https://www.tovlex-example.com/fluid-filtration/sentinel-coolant-recycling-systems/
- we like the way the content is presented on the Tovlex product page - specifically, we like the use of the tabs below the main product images to present a lot of content without it looking overwhelmingly busy.

https://dunmorepanel-example.com/healthcare/westbrook-care-hospital/
- we like the way Dunmore Panel presents their cases studies with a combination of useful information highlighted by informative icons and pictures to present key statistics in the case study. We would like the BrightVane case studies to almost feel like an infographic presentation on the website.

Target Market(s)

Industry/Entity Type

Industrial

Coding

Coded - Design and coding required

Number of Pages Required

3 page

Font styles to use
Sans Serif
Other font styles liked:
• DINPro is used on all collateral - see brand guidelines

Requirements
Must have
• See the brand guidelines file attached for colors and logo usage

```html
<!DOCTYPE html>
<html lang="en">
<head>
<meta charset="utf-8">
<title>BrightVane – Oil Separation and Coolant Recycling</title>
<link rel="stylesheet" href="https://fonts.googleapis.com/css2?family=Rajdhani:wght@500;600;700&family=Poppins:wght@400;500;600&display=swap">
<style>
:root{
  --navy:#0e3a77;
  --navy-deep:#0c1f3d;
  --blue:#1f4b86;
  --green:#7dbb00;
  --ink:#0b1a33;
  --text:#7a8290;
  --rule:#e6e8ec;
  --white:#ffffff;
}
*{box-sizing:border-box;margin:0;padding:0}
html,body{width:1200px;height:3876px;overflow:hidden;background:var(--white)}
body{position:relative;font-family:"Poppins",sans-serif;color:var(--ink)}
.abs{position:absolute}
.btn{position:absolute;background:var(--green);color:var(--white);font-family:"Rajdhani",sans-serif;font-weight:700;letter-spacing:1.5px;font-size:11px;display:flex;align-items:center;justify-content:center;text-transform:uppercase}

/* header */
.site-header{position:absolute;left:0;top:0;width:1200px;height:88px;background:var(--white)}
.brand{position:absolute;display:flex;align-items:center;gap:8px}
.brand-mark{width:50px;height:50px;border-radius:50%;border:4px solid var(--navy)}
.brand-name{font-family:"Rajdhani",sans-serif;font-weight:700;font-size:27px;color:var(--navy)}
.contact{position:absolute;top:10px;font-size:11px;color:var(--green);display:flex;align-items:center;gap:6px}
.topline{position:absolute;left:418px;right:84px;top:36px;border-top:1px solid var(--rule)}
.nav{position:absolute;top:56px;left:420px;display:flex;font-family:"Rajdhani",sans-serif;font-weight:700;font-size:12px;letter-spacing:.5px}
.nav a{color:var(--ink);text-decoration:none;margin-right:43px;position:relative}
.nav a.active{color:var(--green)}
.nav a.active::after{content:"";position:absolute;left:0;right:0;top:24px;height:2px;background:var(--green)}
.estimate{position:absolute;left:990px;top:46px;width:126px;height:32px;background:var(--green);color:var(--white);font-size:10px;font-weight:500;display:flex;align-items:center;justify-content:center}

/* hero */
.hero-photo{position:absolute;left:0;top:88px;width:1200px;height:620px;background:linear-gradient(110deg,#5b6470 0%,#9aa2ab 30%,#cfc4b4 45%,#6e7a88 70%,#3b4654 100%)}
.hero-box{position:absolute;left:585px;top:190px;width:615px;height:295px;background:rgba(22,66,128,.93);padding:40px 0 0 48px;color:var(--white);font-family:"Rajdhani",sans-serif;font-size:50px;line-height:74px}
.hero-box b{font-weight:700}
.hero-box span{font-weight:500}

/* products */
.section-title{position:absolute;left:0;width:1200px;text-align:center;font-family:"Rajdhani",sans-serif;font-weight:700;color:var(--ink)}
.prod-num{position:absolute;font-family:"Rajdhani",sans-serif;font-weight:500;font-size:62px;color:transparent;-webkit-text-stroke:1.3px #c9ced6;line-height:1}
.prod-img{position:absolute;border-radius:6px}
.prod-title{position:absolute;font-family:"Rajdhani",sans-serif;font-weight:600;font-size:31px;color:var(--ink)}
.prod-copy{position:absolute;font-size:11.5px;line-height:24px;color:var(--text)}
.divider{position:absolute;left:168px;width:864px;border-top:1px solid var(--rule)}

/* trusted */
.trusted{position:absolute;left:0;top:1879px;width:1200px;height:134px;background:var(--navy-deep)}
.trusted-label{position:absolute;top:18px;width:100%;text-align:center;font-size:11px;color:var(--white)}
.trusted-name{position:absolute;top:64px;font-family:"Rajdhani",sans-serif;font-weight:700;font-size:22px;color:#9fb3cf}

/* roi */
.roi-art{position:absolute;left:172px;top:2128px;width:410px;height:452px;background:linear-gradient(150deg,#a3abb6 0%,#66717f 50%,#3f4b5c 80%,#8a5a52 100%)}
.roi-title{position:absolute;left:680px;top:2190px;font-family:"Rajdhani",sans-serif;font-weight:700;font-size:58px;color:var(--ink)}

/* case study */
.case{position:absolute;left:0;top:2713px;width:1200px;height:578px;background:linear-gradient(180deg,#224f8c,#1b4680)}
.case-img{position:absolute;left:84px;top:94px;width:680px;height:388px;background:linear-gradient(135deg,#c9ccd0 0%,#8d9399 40%,#5d5347 75%,#3b3630 100%)}
.case-title{position:absolute;left:825px;top:98px;font-family:"Rajdhani",sans-serif;font-weight:700;font-size:31px;line-height:50px;color:var(--white)}
.case-copy{position:absolute;left:825px;top:206px;width:300px;font-size:11.5px;line-height:24px;color:#c9d5e8}
.stat{position:absolute;top:320px}
.stat-value{font-family:"Rajdhani",sans-serif;font-weight:700;font-size:22px;color:var(--green)}
.stat-label{font-size:10.5px;line-height:20px;color:var(--white);margin-top:4px}

/* newsletter */
.eyebrow{position:absolute;left:84px;top:3374px;font-family:"Rajdhani",sans-serif;font-weight:700;font-size:12px;letter-spacing:1px;color:var(--green)}
.news-title{position:absolute;left:84px;top:3392px;font-family:"Rajdhani",sans-serif;font-weight:700;font-size:29px;color:var(--ink)}
.news-sub{position:absolute;left:84px;top:3450px;font-size:11.5px;color:var(--text)}
.news-form{position:absolute;left:612px;top:3400px;width:504px;height:54px;background:#f3f4f6;display:flex}
.news-input{flex:1;padding-left:18px;display:flex;align-items:center;font-size:12px;color:#5a6270}
.news-btn{width:174px;height:50px;margin-top:2px;background:var(--green);color:var(--white);font-family:"Rajdhani",sans-serif;font-weight:700;font-size:12px;letter-spacing:1.5px;display:flex;align-items:center;justify-content:center}

/* footer */
.footer-wave{position:absolute;left:0;top:3520px;width:1200px;height:356px}
.foot-nav{position:absolute;left:84px;top:3720px;display:flex;align-items:center;gap:26px;font-family:"Rajdhani",sans-serif;font-weight:700;font-size:12px;color:var(--white)}
.foot-nav i{width:1px;height:10px;background:var(--white)}
.social{position:absolute;top:3721px;display:flex;gap:16px}
.social span{width:14px;height:14px;border-radius:50%;background:var(--white)}
.foot-small{position:absolute;font-size:11px;color:#b9c7de}
.legal{position:absolute;right:84px;top:3798px;display:flex;gap:16px;font-size:11px;color:#b9c7de}
</style>
</head>
<body>

<header class="site-header">
  <div class="brand" style="left:84px;top:17px">
    <div class="brand-mark"></div>
    <div class="brand-name">BrightVane</div>
  </div>
  <div class="contact" style="left:816px">
    <svg width="12" height="12" viewBox="0 0 24 24"><path fill="#7dbb00" d="M6.6 10.8c1.4 2.8 3.8 5.1 6.6 6.6l2.2-2.2c.3-.3.7-.4 1-.2 1.1.4 2.3.6 3.6.6.6 0 1 .4 1 1V20c0 .6-.4 1-1 1C10.6 21 3 13.4 3 4c0-.6.4-1 1-1h3.5c.6 0 1 .4 1 1 0 1.3.2 2.5.6 3.6.1.3 0 .7-.2 1z"/></svg>
    (555) 014-2290
  </div>
  <div class="contact" style="left:960px">
    <svg width="16" height="12" viewBox="0 0 16 12"><rect width="16" height="12" fill="#7dbb00"/><path d="M0 0l8 6 8-6" stroke="#fff" fill="none"/></svg>
    hello@brightvane-example.com
  </div>
  <div class="topline"></div>
  <nav class="nav">
    <a class="active">PRODUCT</a><a>BENEFITS</a><a>INDUSTRIES SERVED</a><a>ABOUT US</a><a>SERVICE &amp; SUPPORT</a>
  </nav>
  <div class="estimate">Request an Estimate</div>
</header>

<section class="hero">
  <div class="hero-photo" role="img" aria-label="Engineer in a hard hat and safety vest on a factory floor"></div>
  <div class="hero-box"><b>The Global Leader</b><br><span>in Oil Separation</span><br><span>and Coolant Recycling</span></div>
  <svg class="abs" style="left:0;top:560px" width="1200" height="150" viewBox="0 0 1200 150">
    <path d="M0 28 Q600 170 1200 28 L1200 150 L0 150Z" fill="#fff"/>
    <path d="M0 28 Q600 170 1200 28" stroke="#0e3a77" stroke-width="8" fill="none"/>
    <path d="M0 36 Q600 178 1200 36" stroke="#7dbb00" stroke-width="6" fill="none"/>
  </svg>
</section>

<section class="products">
  <h2 class="section-title" style="top:788px;font-size:56px">Our Product</h2>

  <div class="prod-num" style="left:258px;top:945px">01</div>
  <div class="prod-img" style="left:322px;top:965px;width:196px;height:145px;background:linear-gradient(135deg,#2d4ea8,#1b3070 70%,#d7d9dd)" role="img" aria-label="Coolant recycling system unit"></div>
  <div class="prod-title" style="left:523px;top:940px">Coolant Recycling Systems</div>
  <p class="prod-copy" style="left:523px;top:994px;width:450px">The FluidCycle™ Coolant Recycling Systems Are Based On Decades-Long Successful Fluid Treatment Practices, Using The Award-Winning, Multipatented BrightVane® Systems Approach To Solving Problems.</p>
  <div class="btn" style="left:523px;top:1091px;width:125px;height:38px">Learn More</div>

  <div class="divider" style="top:1192px"></div>

  <div class="prod-title" style="left:294px;top:1278px">Magnetic Separators</div>
  <p class="prod-copy" style="left:294px;top:1332px;width:420px">BrightVane Magnetic Separators Fit With Our Core Philosophies: Providing Products That Eliminate The Use Of Filter Consumables, Are Easy To Implement, Simple To Operate, And Re</p>
  <div class="btn" style="left:294px;top:1429px;width:125px;height:38px">Learn More</div>
  <div class="prod-img" style="left:752px;top:1260px;width:106px;height:160px;background:linear-gradient(180deg,#e4e7ea,#9ca6b0 55%,#2d5db0)" role="img" aria-label="Magnetic separator units"></div>
  <div class="prod-num" style="left:872px;top:1268px">02</div>

  <div class="divider" style="top:1530px"></div>

  <div class="prod-num" style="left:258px;top:1607px">01</div>
  <div class="prod-img" style="left:322px;top:1627px;width:196px;height:145px;background:linear-gradient(135deg,#2d4ea8,#1b3070 70%,#d7d9dd)" role="img" aria-label="Oil water separator unit"></div>
  <div class="prod-title" style="left:523px;top:1602px">Oil Water Separators</div>
  <p class="prod-copy" style="left:523px;top:1656px;width:400px">The BrightVane "Non-Clogging" Design Allows For The Separation Of Oils And Settling Of Solids In One Step.</p>
  <div class="btn" style="left:523px;top:1728px;width:125px;height:38px">Learn More</div>
</section>

<section class="trusted">
  <div class="trusted-label">Trusted By</div>
  <div class="trusted-name" style="left:240px">Halberd</div>
  <div class="trusted-name" style="left:420px">Corvane</div>
  <div class="trusted-name" style="left:560px">Stellmark</div>
  <div class="trusted-name" style="left:722px">Aerolith</div>
  <div class="trusted-name" style="left:922px">Weftline</div>
</section>

<section class="roi">
  <div class="roi-art" role="img" aria-label="Illustration of recycling arrows framing an engineer at a plant"></div>
  <h2 class="roi-title">ROI Calculator</h2>
  <p class="prod-copy" style="left:680px;top:2284px;width:330px">By Drastically Reducing Coolant Costs And The Cost Of Waste Removal, Our Typical Systems Pay For Themselves In 6-9 Months. Check Ot Our ROI Calculator To Determine How Much You Can Savie With Our Coolant Recycling Systems.</p>
  <div class="btn" style="left:680px;top:2436px;width:175px;height:50px">Learn More</div>
</section>

<section class="case">
  <div class="case-img" role="img" aria-label="CNC milling cutter working metal with chips on the table"></div>
  <h3 class="case-title">Kestrel Ridge<br>Machining</h3>
  <p class="case-copy">Learn How Kestrel Ridge Machining Saved 35-45% On Their Coolant Recycling While Increasing Employee Morale With A Fully Automated BrightVane Recycling System</p>
  <div class="stat" style="left:825px"><div class="stat-value">35-45%</div><div class="stat-label">Reduced Coolant<br>Costs</div></div>
  <div class="abs" style="left:955px;top:320px;width:1px;height:64px;background:rgba(255,255,255,.3)"></div>
  <div class="stat" style="left:998px"><div class="stat-value">100%</div><div class="stat-label">Employee<br>Morale</div></div>
  <div class="btn" style="left:825px;top:423px;width:175px;height:48px">Learn More</div>
</section>

<section class="newsletter">
  <div class="eyebrow">SIGN UP</div>
  <h3 class="news-title">STAY UP TO DATE WITH BRIGHTVANE</h3>
  <p class="news-sub">By Drastically Reducing Coolant Costs And The Cost</p>
  <div class="news-form"><div class="news-input">Enter email address</div><div class="news-btn">SUBSCRIBE</div></div>
</section>

<footer>
  <svg class="footer-wave" viewBox="0 0 1200 356">
    <path d="M0 20 Q600 180 1200 20 L1200 356 L0 356Z" fill="#0e3a77"/>
    <path d="M0 18 Q600 178 1200 18" stroke="#7dbb00" stroke-width="5" fill="none"/>
  </svg>
  <nav class="foot-nav"><span>CONTACT</span><i></i><span>ABOUT</span><i></i><span>BLOGS</span></nav>
  <div class="brand" style="left:530px;top:3706px">
    <div class="brand-mark" style="width:38px;height:38px;border:3px solid #fff"></div>
    <div class="brand-name" style="color:#fff;font-size:21px">BrightVane</div>
  </div>
  <div class="social" style="left:1034px"><span></span><span></span><span></span></div>
  <div class="foot-small" style="left:84px;top:3798px">410 Foundry Road • Milltown, PA 19000</div>
  <div class="foot-small" style="left:84px;top:3820px">© 2021 Northgate Steelworks. All Rights Reserved</div>
  <div class="legal"><span>Terms Of Service</span><span>|</span><span>Privacy Policy</span><span>|</span><span>Sitemap</span></div>
</footer>

</body>
</html>
```